Packaging designed for both the bar and the box for retail and online sales

The name of the product is Plum Crumb. We manufacture a consumer package good product that's a healthy edible cookie dough bar. The product look, feels and tastes like cookie dough. It's sold in the refrigerator section of retail stores next to cookie dough and golden slab. The product is Gluten Free, Diary Free and include B-12, Biotin and Collagen. The ingredients are natural. When design this think about who eat cookie dough and how to engage the buyer in purchasing the product.

We needs design packaging designed for both the bar and the box. I have attached the die lines for both products.

Target Market(s)

Our customer is 16-45. Primarily female but really anyone. Middle to upper income. Interest include healthy life style and yoga. Like to eat something sweet but not feel guilty.

Colors

Designer to choose colors to be used in the design.

Requirements
Must have
• Must be clean, warm, inviting. Brand designs I really like are Golden Slab.
Should not have
• Should not have a photo of food

```html
<!DOCTYPE html>
<html lang="en">
<head>
<meta charset="UTF-8">
<title>Plum Crumb – Bar Wrappers</title>
<link rel="stylesheet" href="https://fonts.googleapis.com/css2?family=Archivo+Black&display=swap">
<style>
  :root {
    --bg: #ffffff;
    --navy: #1e3a94;
    --navy-deep: #182f7c;
    --orange: #f8b347;
    --orange-soft: #f6a93a;
    --plum: #4b3578;
    --plum-deep: #3f2b69;
    --lime: #c4ee83;
    --lime-soft: #b6e574;
  }
  * { box-sizing: border-box; margin: 0; padding: 0; }
  html, body {
    width: 1200px; height: 1200px; overflow: hidden;
    background: var(--bg);
    font-family: "Archivo Black", "Arial Black", sans-serif;
  }
  .canvas {
    position: relative; width: 1200px; height: 1200px;
    display: flex; justify-content: center; align-items: center; gap: 90px;
  }
  .wrapper {
    position: relative; width: 330px; height: 560px;
    display: flex; flex-direction: column;
    border-radius: 4px; overflow: hidden;
    box-shadow: 0 18px 30px rgba(0,0,0,0.08);
  }
  .crimp {
    height: 22px; flex: none;
    background-image: repeating-linear-gradient(90deg, rgba(255,255,255,0.12) 0 2px, rgba(0,0,0,0.08) 2px 5px);
  }
  .top-panel {
    flex: 0 0 222px; position: relative;
    padding: 56px 0 0 0;
  }
  .claims {
    display: flex; align-items: center; justify-content: flex-end;
    gap: 8px; padding-right: 60px;
  }
  .claim-badge {
    width: 22px; height: 22px; border-radius: 50%;
    border: 2px solid var(--accent);
  }
  .claim-badge.solid { width: 26px; height: 26px; background: var(--accent); border: none; }
  .claim-label { font-size: 13px; color: var(--accent); letter-spacing: 0.02em; }
  .bottom-panel { flex: 1; position: relative; }
  .pattern-field {
    position: absolute; inset: 0;
  }
  .brand-name {
    position: absolute; top: 14px; left: 0; right: 0;
    text-align: center; color: var(--ink);
    font-size: 52px; line-height: 0.95; letter-spacing: 0.01em;
    text-transform: uppercase;
  }
  .flavour {
    position: absolute; top: 176px; left: 0; right: 0; text-align: center;
    color: var(--ink); font-size: 15px; letter-spacing: 0.02em;
  }
  .net-weight {
    position: absolute; top: 198px; left: 0; right: 0; text-align: center;
    color: var(--ink); font-size: 9px; letter-spacing: 0.03em;
  }
  .wrapper--navy { --ink: var(--navy); --accent: var(--orange); }
  .wrapper--navy .crimp-top, .wrapper--navy .top-panel { background: linear-gradient(160deg, var(--navy), var(--navy-deep)); }
  .wrapper--navy .pattern-field { background: linear-gradient(180deg, var(--orange), var(--orange-soft)); }
  .wrapper--navy .crimp-bottom { background-color: var(--orange-soft); }
  .wrapper--plum { --ink: var(--plum); --accent: var(--lime); }
  .wrapper--plum .crimp-top, .wrapper--plum .top-panel { background: linear-gradient(160deg, var(--plum), var(--plum-deep)); }
  .wrapper--plum .pattern-field { background: linear-gradient(180deg, var(--lime), var(--lime-soft)); }
  .wrapper--plum .crimp-bottom { background-color: var(--lime-soft); }
</style>
</head>
<body>
<main class="canvas">
  <article class="wrapper wrapper--navy">
    <div class="crimp crimp-top"></div>
    <section class="top-panel">
      <div class="claims">
        <span class="claim-badge"></span>
        <span class="claim-badge"></span>
        <span class="claim-badge solid"></span>
        <span class="claim-label">BIOTIN</span>
      </div>
    </section>
    <section class="bottom-panel">
      <div class="pattern-field" role="img" aria-label="Repeating pattern of small cookie illustrations"></div>
      <h2 class="brand-name">Plum<br>Crumb</h2>
      <p class="flavour">BLUEBERRY</p>
      <p class="net-weight">NET WT 2.5G</p>
    </section>
    <div class="crimp crimp-bottom"></div>
  </article>

  <article class="wrapper wrapper--plum">
    <div class="crimp crimp-top"></div>
    <section class="top-panel">
      <div class="claims">
        <span class="claim-badge"></span>
        <span class="claim-badge"></span>
        <span class="claim-badge solid"></span>
        <span class="claim-label">BIOTIN</span>
      </div>
    </section>
    <section class="bottom-panel">
      <div class="pattern-field" role="img" aria-label="Repeating pattern of small cookie illustrations"></div>
      <h2 class="brand-name">Plum<br>Crumb</h2>
      <p class="flavour">BLUEBERRY</p>
      <p class="net-weight">NET WT 2.5G</p>
    </section>
    <div class="crimp crimp-bottom"></div>
  </article>
</main>
</body>
</html>
```